Website for Plumbing Company, Sir FlowBoiler

I need a 7-page fully HTML-coded website for my plumbing company, Sir FlowBoiler. We specialize in installation, repair, and replacement of both gas and electric water heaters. Although we offer both tankless (on-demand) water heaters and standard (with tank) water heaters, most of our business is related to standard (with tank) water heaters in the USA market.

These are the pages I need:
1. Home page with sections such as About Us, Our Services, Why Choose Us, Testimonials, Location Map (Palm Beach County Florida), Quote Request Form, Join Our Newsletter, Mission Statement, etc.

2. Gas Water Heaters

3. Electric Water Heaters

4. Tankless Water Heaters

5. About Us

6. Contact Us

7. Privacy Policy, Terms & Conditions

Be sure to mention the following points:
1. Same-Day Service
2. Best Price Guarantee
3. 100% Satisfaction Rating
4. 15-Year Warranty on Water Heater & Parts
5. Lifetime Warranty on Workmanship
*All Warranties are Transferrable Upon Home Sale

Once design is selected and finalized, I need the website coded in a standard HTML/CSS and temporarily hosted on your development server so I can see the website functionality that is not observable from screenshots, such as section animations, etc. Once those details are finalized, I will move the source code to my server and complete the project.

Target Market(s)

Residential Home Owners and Business Owners

Industry/Entity Type

Plumbing, Home Services, Remodeling, Construction

Coding

Coded - Design and coding required

Number of Pages Required

5+ page

Colors
0054AA
0677BA
7BADD7
CADEEF
E8F1F8
FFC000
F8CF3A
FAE287
FDF2CF
FEFAEE
EE7325
F08F49
F5BC92
FAE3D3
FDF4ED

Requirements
Must have
• Clean, colorful, and professional

```html
<!DOCTYPE html>
<html lang="en">
<head>
<meta charset="utf-8">
<title>Sir FlowBoiler — Website Pages</title>
<link href="https://fonts.googleapis.com/css2?family=Poppins:wght@500;600;700;800&family=Inter:wght@400;500;600;700&display=swap" rel="stylesheet">
<style>
:root{
  --stage:#121212;
  --page:#eef1f5;
  --white:#ffffff;
  --blue:#0054AA;
  --blue-2:#0677BA;
  --sky:#7BADD7;
  --ice:#E8F1F8;
  --navy:#10233f;
  --ink:#3a4553;
  --muted:#7d8896;
  --line:#dfe4ea;
  --orange:#EE7325;
  --orange-soft:#FAE3D3;
  --yellow:#FFC000;
}
*{box-sizing:border-box;margin:0;padding:0}
html,body{width:1200px;height:328px;overflow:hidden;background:var(--stage)}
body{position:relative;font-family:"Inter",sans-serif;color:var(--ink);font-size:3px;line-height:1.3}

.page{position:absolute;top:11px;height:311px;background:var(--page);overflow:hidden;display:flex;flex-direction:column}
.page-home{left:22px;width:250px}
.page-gas{left:306px;width:246px}
.page-tankless{left:588px;width:246px}
.page-legal{left:868px;width:284px}

/* header */
.site-header{height:18px;flex:none;background:var(--white);display:flex;align-items:center;padding:0 8px;gap:6px;border-bottom:1px solid var(--line)}
.brand{display:flex;align-items:center;gap:2px;font-family:"Poppins",sans-serif;font-weight:700;font-size:4.4px;color:var(--blue);white-space:nowrap}
.brand-dot{width:8px;height:8px;border-radius:50%;background:var(--blue)}
.main-nav{margin-left:auto;display:flex;gap:7px;font-size:3.2px;color:var(--navy)}
.main-nav .active{color:var(--orange)}
.search-icon{width:5px;height:5px}
.btn-quote{background:var(--orange);color:var(--white);font-size:2.9px;font-weight:600;padding:2px 4px;border-radius:1px;white-space:nowrap}

/* hero */
.hero{position:relative;flex:none;height:65px;overflow:hidden}
.hero-bg{position:absolute;inset:0;background:linear-gradient(90deg,#f3f2ef 0%,#e7e3dd 45%,#cfcac3 100%)}
.hero-photo{position:absolute;top:0;bottom:0;width:64px;background:linear-gradient(180deg,#e2ddd6 0%,#cfc9c2 100%)}
.hero-content{position:relative;padding:9px 0 0 8px}
.hero-tag{display:block;width:fit-content;background:var(--orange);color:var(--white);font-size:2.4px;line-height:1.2;font-weight:600;padding:1px 3px;border-radius:1px}
.hero-title{font-family:"Poppins",sans-serif;font-weight:800;color:var(--navy);font-size:11.5px;line-height:1.05;margin-top:3px;letter-spacing:-.2px}
.hero-actions{display:flex;gap:4px;margin-top:5px}
.btn{font-size:2.5px;line-height:1.2;font-weight:600;padding:2px 5px;border-radius:1px;white-space:nowrap}
.btn-primary{background:var(--blue);color:var(--white)}
.btn-outline{background:var(--white);color:var(--orange);border:.5px solid var(--orange)}

/* service band */
.service-band{flex:none;background:var(--blue);padding:7px 8px 6px}
.band-row{display:flex;align-items:center;justify-content:space-between;gap:4px}
.band-title{font-family:"Poppins",sans-serif;font-weight:700;color:var(--white);font-size:5px;white-space:nowrap}
.band-stats{display:flex;gap:4px}
.stat{text-align:center;color:var(--white);font-size:2px;line-height:1.3;white-space:nowrap}
.stat b{display:block;color:var(--yellow);font-size:2.8px;font-weight:700}
.service-cards{display:grid;grid-template-columns:repeat(3,1fr);gap:6px;margin-top:6px;padding:0 3px}
.service-card{background:var(--white);height:42px;border-radius:1px;text-align:center;padding:4px 3px 0;position:relative}
.service-icon{width:10px;height:10px;margin:0 auto;display:block}
.service-card h3{font-size:3.1px;font-weight:700;color:var(--navy);margin-top:2px}
.service-card p{font-size:2.1px;color:var(--muted);line-height:1.35;margin-top:1.5px}
.service-card .card-link{position:absolute;left:6px;right:6px;bottom:3px;font-size:2.3px;color:var(--blue);border-top:.5px solid var(--line);padding-top:1.5px}

/* shared blocks */
.panel{background:var(--white);border-radius:1px}
.section-title{font-family:"Poppins",sans-serif;font-weight:700;color:var(--navy);font-size:4.6px;line-height:1.25}
.copy{font-size:2.2px;line-height:1.45;color:var(--muted)}
.photo{border-radius:1px}

/* home: feature strip */
.feature-strip{display:flex;justify-content:space-around;padding:8px 10px;height:30px;align-items:center}
.feature{display:flex;gap:2px;align-items:center;font-size:2.2px;line-height:1.3;color:var(--ink);width:36px}
.feature svg{width:5px;height:5px;flex:none}

/* comparison */
.compare{margin:0 10px;padding:5px 7px;height:50px}
.compare .section-title{text-align:center;font-size:4.2px}
.compare-grid{display:grid;grid-template-columns:1.2fr 1fr 1fr 1fr;gap:5px;margin-top:4px}
.compare-col{text-align:center;font-size:2.2px;color:var(--ink)}
.compare-col .plan{display:block;background:var(--blue);color:var(--white);font-weight:600;padding:2px 0;margin-top:2px}
.compare-col .price{display:block;font-weight:700;color:var(--navy);font-size:3.4px;margin-top:3px}
.benefit-list{list-style:none;font-size:2.2px;line-height:1.5;color:var(--ink)}
.benefit-list strong{display:block;color:var(--navy);font-size:2.6px}

.home-heading{margin:14px 0 0 12px;font-size:4.8px}
.about-card{margin:5px 10px 0;height:52px;display:flex;gap:6px;padding:3px}
.about-card .photo{width:62px;flex:none;background:linear-gradient(160deg,#dadde1,#9ea4ab)}
.about-card h4{font-size:2.8px;color:var(--navy);margin-bottom:2px}

/* gas page */
.gas-main{margin:8px 10px 0;padding:6px 8px;height:92px}
.gas-table{display:grid;grid-template-columns:1.3fr 1fr 1fr 1fr;gap:4px;margin-top:4px}
.key-benefits{margin-top:6px;border-top:.5px solid var(--line);padding-top:4px}
.key-benefits .section-title{font-size:4px}
.benefit-columns{display:grid;grid-template-columns:1fr 1fr;gap:8px;margin-top:2px}
.book-card{margin:4px 10px 0;padding:5px 8px;height:62px}
.book-row{display:flex;gap:6px;margin-top:4px}
.book-row .photo{width:60px;height:36px;flex:none;background:linear-gradient(160deg,#d7dade,#9aa0a7)}
.book-row h4{font-size:2.8px;color:var(--navy);margin-bottom:2px}

/* tankless page */
.tankless-photo{position:absolute;top:0;right:0;width:116px;height:100%;background:linear-gradient(90deg,#c8cacd,#e9e9e7 40%,#b9bbbe)}
.how-works{padding:7px 12px 6px;height:72px}
.products{display:grid;grid-template-columns:repeat(3,1fr);gap:10px;margin-top:4px}
.product{text-align:center;font-size:2.1px;color:var(--muted)}
.product-photo{height:36px;width:28px;margin:2px auto;background:linear-gradient(90deg,#8f959b,#dcdfe2 50%,#8f959b)}
.estimate-card{margin:0 8px;padding:5px 7px;height:48px}
.estimate-row{display:flex;gap:5px;margin-top:4px}
.estimate-row svg{width:9px;height:9px;flex:none}
.estimate-row h4{font-size:2.7px;color:var(--navy);margin-bottom:1.5px}
.contact-card{margin:6px 8px 0;padding:5px 7px;height:40px}
.contact-row{display:flex;gap:6px;margin-top:4px}
.map{width:26px;height:16px;flex:none;background:linear-gradient(135deg,#d8e6cf,#c7d9e8)}

/* legal page */
.hero-legal{height:84px}
.hero-legal .hero-bg{background:linear-gradient(90deg,#eceef0,#d9dcde)}
.van-photo{position:absolute;top:0;bottom:0;left:140px;right:0;background:linear-gradient(180deg,#e6e8ea 0%,#d3d6d9 100%)}
.quote-form{position:relative;margin:5px 0 0 8px;width:114px;background:rgba(255,255,255,.92);padding:4px 5px}
.quote-form h1{font-family:"Poppins",sans-serif;font-weight:700;color:var(--navy);font-size:8px;line-height:1.05}
.form-label{font-size:2.2px;color:var(--muted);margin-top:3px}
.form-input{height:6px;border:.5px solid var(--line);background:var(--white);font-size:2.2px;line-height:1.2;color:var(--muted);padding:1.3px 2px;margin-top:2px}
.cta-row{flex:none;display:flex;gap:5px;align-items:center;padding:5px 10px 0}
.cta-row .btn-primary{font-size:2.3px}
.cta-row .link{font-size:2.3px;color:var(--orange)}
.trust-row{display:flex;gap:14px;padding:4px 12px}
.trust{display:flex;gap:2px;align-items:center;font-size:2.2px;line-height:1.3}
.trust svg{width:5px;height:5px}
.legal-grid{display:grid;grid-template-columns:1fr 1fr;gap:6px;padding:3px 10px 0}
.legal-card{padding:5px 6px;height:104px}
.legal-card .section-title{font-size:4.2px;margin-bottom:3px}
.legal-card .copy + .copy{margin-top:2px}
.btn-orange{display:inline-block;background:var(--orange);color:var(--white);font-size:2.3px;line-height:1.2;font-weight:600;padding:2px 4px;margin-top:4px}
.notice-box{background:var(--ice);padding:3px;margin-top:3px}
.notice-box strong{display:block;font-size:2.4px;color:var(--navy);margin-bottom:1px}
.legal-card.short{height:74px;margin-top:0}
.warranty-photo{height:40px;margin-top:3px;background:linear-gradient(180deg,#e4e7ea 0%,#c9d3de 100%)}
</style>
</head>
<body>

<!-- Home page -->
<article class="page page-home">
  <header class="site-header">
    <span class="brand"><i class="brand-dot"></i>Sir FlowBoiler</span>
    <nav class="main-nav"><span class="active">Home</span><span>Gas</span><span>Electric</span><span>About</span><span>Tankless</span></nav>
    <span class="btn-quote">Get a Quote</span>
  </header>
  <section class="hero">
    <div class="hero-bg" role="img" aria-label="Bright kitchen interior, softly blurred"></div>
    <div class="hero-photo" style="right:22px" role="img" aria-label="Photo of a smiling plumber in work uniform"></div>
    <div class="hero-content">
      <span class="hero-tag">Same-Day Water Heater Service</span>
      <h1 class="hero-title">Hot Water Today,<br>Guaranteed</h1>
      <div class="hero-actions"><span class="btn btn-primary">Call Now: Same-Day Service</span><span class="btn btn-outline">Free Estimate</span></div>
    </div>
  </section>
  <section class="service-band">
    <div class="band-row">
      <h2 class="band-title">Expert Solutions for Every Home</h2>
      <div class="band-stats">
        <div class="stat"><b>15-Year</b>Heater &amp; Parts</div>
        <div class="stat"><b>Lifetime</b>Workmanship</div>
        <div class="stat"><b>Best Price</b>Guarantee</div>
        <div class="stat"><b>Same-Day</b>Service</div>
      </div>
    </div>
    <div class="service-cards">
      <div class="service-card">
        <svg class="service-icon" viewBox="0 0 20 20"><circle cx="10" cy="10" r="9" fill="none" stroke="#EE7325" stroke-width="1.4"/><path d="M10 4c2 3 4 4 4 7a4 4 0 0 1-8 0c0-2 1-3 2-4 0 2 1 2 2 2 0-2-1-3 0-5z" fill="#EE7325"/></svg>
        <h3>Gas Water Heaters</h3>
        <p>Fast installs and repairs for gas tank heaters.</p>
        <span class="card-link">Learn More →</span>
      </div>
      <div class="service-card">
        <svg class="service-icon" viewBox="0 0 20 20"><circle cx="10" cy="10" r="9" fill="none" stroke="#EE7325" stroke-width="1.4"/><path d="M11 3 6 11h4l-1 6 5-8h-4z" fill="#EE7325"/></svg>
        <h3>Electric Heaters</h3>
        <p>Reliable electric tank service for every home.</p>
        <span class="card-link">Learn More →</span>
      </div>
      <div class="service-card">
        <svg class="service-icon" viewBox="0 0 20 20"><circle cx="10" cy="10" r="9" fill="none" stroke="#EE7325" stroke-width="1.4"/><path d="M10 4c2 3 4 4 4 7a4 4 0 0 1-8 0c0-2 1-3 2-4 0 2 1 2 2 2 0-2-1-3 0-5z" fill="#EE7325"/></svg>
        <h3>Tankless Heaters</h3>
        <p>On-demand hot water with lower energy bills.</p>
        <span class="card-link">Learn More →</span>
      </div>
    </div>
  </section>
  <div class="feature-strip">
    <div class="feature"><svg viewBox="0 0 10 10"><circle cx="5" cy="5" r="4.5" fill="#EE7325"/><path d="M3 5l1.5 1.5L7 3.5" stroke="#fff" fill="none"/></svg>Same-Day Service</div>
    <div class="feature"><svg viewBox="0 0 10 10"><circle cx="5" cy="5" r="4.5" fill="#EE7325"/><path d="M3 5l1.5 1.5L7 3.5" stroke="#fff" fill="none"/></svg>Best Price Guarantee</div>
    <div class="feature"><svg viewBox="0 0 10 10"><circle cx="5" cy="5" r="4.5" fill="#EE7325"/><path d="M3 5l1.5 1.5L7 3.5" stroke="#fff" fill="none"/></svg>100% Satisfaction Rating</div>
    <div class="feature"><svg viewBox="0 0 10 10"><circle cx="5" cy="5" r="4.5" fill="#EE7325"/><path d="M3 5l1.5 1.5L7 3.5" stroke="#fff" fill="none"/></svg>Transferable Warranties</div>
  </div>
  <section class="panel compare">
    <h2 class="section-title">Cost to Operate Comparison</h2>
    <div class="compare-grid">
      <ul class="benefit-list"><li><strong>Key Benefits</strong></li><li>Lower monthly bills</li><li>Faster recovery</li><li>Longer tank life</li></ul>
      <div class="compare-col">Gas Tank<span class="plan">Standard</span><span class="price">$15.90</span></div>
      <div class="compare-col">Electric Tank<span class="plan">Standard</span><span class="price">$19.90</span></div>
      <div class="compare-col">Tankless<span class="plan">On-Demand</span><span class="price">$9.90</span></div>
    </div>
  </section>
  <h2 class="section-title home-heading">Same-Day Gas Water Heater Service</h2>
  <section class="panel about-card">
    <div class="photo" role="img" aria-label="Standard tank water heater installed in a utility room"></div>
    <div>
      <h4>About Us</h4>
      <p class="copy"><strong>Our Team Serves Palm Beach County</strong><br>We install, repair and replace gas and electric water heaters for homes and businesses. Every job is backed by a 15-year warranty on heater and parts, plus lifetime workmanship coverage.</p>
    </div>
  </section>
</article>

<!-- Gas water heaters page -->
<article class="page page-gas">
  <header class="site-header">
    <span class="brand"><i class="brand-dot"></i>Sir FlowBoiler</span>
    <nav class="main-nav"><span class="active">Home</span><span>Gas</span><span>Electric</span><span>About</span><span>Tankless</span></nav>
    <svg class="search-icon" viewBox="0 0 10 10"><circle cx="4" cy="4" r="3" fill="none" stroke="#10233f"/><path d="M6.2 6.2 9 9" stroke="#10233f"/></svg>
    <span class="btn-quote">Get a Quote</span>
  </header>
  <section class="hero">
    <div class="hero-bg" role="img" aria-label="Bright kitchen interior, softly blurred"></div>
    <div class="hero-photo" style="right:20px" role="img" aria-label="Photo of a smiling plumber in work uniform"></div>
    <div class="hero-content">
      <span class="hero-tag">Gas Water Heater Experts</span>
      <h1 class="hero-title">Hot Water Today,<br>Guaranteed</h1>
      <div class="hero-actions"><span class="btn btn-primary">Book Same-Day Repair</span><span class="btn btn-outline">Free Estimate</span></div>
    </div>
  </section>
  <section class="service-band">
    <div class="band-row">
      <h2 class="band-title">Expert Solutions for Every Home</h2>
      <div class="band-stats">
        <div class="stat"><b>15-Year</b>Parts</div>
        <div class="stat"><b>Lifetime</b>Labor</div>
        <div class="stat"><b>Best Price</b>Guarantee</div>
        <div class="stat"><b>100%</b>Satisfaction</div>
      </div>
    </div>
    <div class="service-cards">
      <div class="service-card">
        <svg class="service-icon" viewBox="0 0 20 20"><circle cx="10" cy="10" r="9" fill="none" stroke="#EE7325" stroke-width="1.4"/><path d="M10 4c2 3 4 4 4 7a4 4 0 0 1-8 0c0-2 1-3 2-4 0 2 1 2 2 2 0-2-1-3 0-5z" fill="#EE7325"/></svg>
        <h3>Gas Water Heaters</h3>
        <p>Safe venting, gas lines and pilot repairs.</p>
        <span class="card-link">Learn More →</span>
      </div>
      <div class="service-card">
        <svg class="service-icon" viewBox="0 0 20 20"><circle cx="10" cy="10" r="9" fill="none" stroke="#EE7325" stroke-width="1.4"/><path d="M11 3 6 11h4l-1 6 5-8h-4z" fill="#EE7325"/></svg>
        <h3>Electric Heaters</h3>
        <p>Elements, thermostats and full replacements.</p>
        <span class="card-link">Learn More →</span>
      </div>
      <div class="service-card">
        <svg class="service-icon" viewBox="0 0 20 20"><circle cx="10" cy="10" r="9" fill="none" stroke="#EE7325" stroke-width="1.4"/><path d="M10 4c2 3 4 4 4 7a4 4 0 0 1-8 0c0-2 1-3 2-4 0 2 1 2 2 2 0-2-1-3 0-5z" fill="#EE7325"/></svg>
        <h3>Tankless Heaters</h3>
        <p>Compact on-demand units sized for you.</p>
        <span class="card-link">Learn More →</span>
      </div>
    </div>
  </section>
  <section class="panel gas-main">
    <h2 class="section-title">Cost to Operate Comparison</h2>
    <div class="gas-table">
      <ul class="benefit-list"><li><strong>Gas Benefits</strong></li><li>Heats water faster</li><li>Works in outages</li><li>Lower fuel costs</li><li>Proven tank design</li></ul>
      <div class="compare-col">40 Gal Gas<span class="plan">Standard</span><span class="price">$15.90</span></div>
      <div class="compare-col">50 Gal Gas<span class="plan">Standard</span><span class="price">$19.90</span></div>
      <div class="compare-col">Tankless<span class="plan">On-Demand</span><span class="price">$9.90</span></div>
    </div>
    <div class="key-benefits">
      <h3 class="section-title">Key Benefits</h3>
      <div class="benefit-columns">
        <ul class="benefit-list"><li>15-year warranty on heater and parts</li><li>Lifetime warranty on workmanship</li><li>Warranties transfer upon home sale</li></ul>
        <ul class="benefit-list"><li><strong>Our Gas Heater Promise</strong></li><li>Licensed technicians arrive the same day and leave your home clean.</li></ul>
      </div>
    </div>
  </section>
  <section class="panel book-card">
    <h2 class="section-title">Book Same-Day Service</h2>
    <div class="book-row">
      <div class="photo" role="img" aria-label="Gas tank water heater in a garage"></div>
      <div>
        <h4>One Stop Hot Water Service</h4>
        <p class="copy">Call before noon and we install your new gas water heater today, with the best price guaranteed.</p>
      </div>
    </div>
  </section>
</article>

<!-- Tankless water heaters page -->
<article class="page page-tankless">
  <header class="site-header">
    <span class="brand"><i class="brand-dot"></i>Sir FlowBoiler</span>
    <nav class="main-nav"><span class="active">Home</span><span>Gas</span><span>Electric</span><span>About</span><span>Tankless</span></nav>
    <span class="btn-quote">Get a Quote</span>
  </header>
  <section class="hero">
    <div class="hero-bg" role="img" aria-label="Light utility room wall"></div>
    <div class="tankless-photo" role="img" aria-label="Tank water heaters installed in a utility room"></div>
    <div class="hero-content">
      <span class="hero-tag">On-Demand Tankless Systems</span>
      <h1 class="hero-title">Endless Hot Water &amp;<br>Hot Tankless</h1>
      <div class="hero-actions"><span class="btn btn-primary">Schedule Installation</span><span class="btn btn-outline">Free Estimate</span></div>
    </div>
  </section>
  <section class="service-band">
    <div class="band-row">
      <h2 class="band-title">Expert Solutions for Every Home</h2>
      <div class="band-stats">
        <div class="stat"><b>Same-Day</b>Service</div>
        <div class="stat"><b>15-Year</b>Warranty</div>
        <div class="stat"><b>Lifetime</b>Labor</div>
      </div>
    </div>
    <div class="service-cards">
      <div class="service-card">
        <svg class="service-icon" viewBox="0 0 20 20"><circle cx="10" cy="10" r="9" fill="none" stroke="#EE7325" stroke-width="1.4"/><path d="M10 4c2 3 4 4 4 7a4 4 0 0 1-8 0c0-2 1-3 2-4 0 2 1 2 2 2 0-2-1-3 0-5z" fill="#EE7325"/></svg>
        <h3>Gas Water Heaters</h3>
        <p>Gas-fired tankless units with high output.</p>
        <span class="card-link">Learn More →</span>
      </div>
      <div class="service-card">
        <svg class="service-icon" viewBox="0 0 20 20"><circle cx="10" cy="10" r="9" fill="none" stroke="#EE7325" stroke-width="1.4"/><path d="M11 3 6 11h4l-1 6 5-8h-4z" fill="#EE7325"/></svg>
        <h3>Electric Heaters</h3>
        <p>Electric tankless units for smaller homes.</p>
        <span class="card-link">Learn More →</span>
      </div>
      <div class="service-card">
        <svg class="service-icon" viewBox="0 0 20 20"><circle cx="10" cy="10" r="9" fill="none" stroke="#EE7325" stroke-width="1.4"/><path d="M10 4c2 3 4 4 4 7a4 4 0 0 1-8 0c0-2 1-3 2-4 0 2 1 2 2 2 0-2-1-3 0-5z" fill="#EE7325"/></svg>
        <h3>Tankless Heaters</h3>
        <p>Descaling, flushing and yearly upkeep.</p>
        <span class="card-link">Learn More →</span>
      </div>
    </div>
  </section>
  <section class="how-works">
    <h2 class="section-title">How the System Works</h2>
    <div class="products">
      <div class="product">Compact Gas Unit<div class="product-photo" role="img" aria-label="Wall-mounted gas tankless water heater"></div>Heats on demand</div>
      <div class="product">Electric Inline Unit<div class="product-photo" role="img" aria-label="Wall-mounted electric tankless water heater"></div>Heats on demand</div>
      <div class="product">Whole Home Unit<div class="product-photo" role="img" aria-label="Large whole-home tankless water heater"></div>Heats on demand</div>
    </div>
  </section>
  <section class="panel estimate-card">
    <h2 class="section-title">Estimates in Store Now</h2>
    <div class="estimate-row">
      <svg viewBox="0 0 20 20"><circle cx="10" cy="10" r="9.5" fill="#EE7325"/><path d="M6 10l3 3 5-6" stroke="#fff" stroke-width="1.8" fill="none"/></svg>
      <div>
        <h4>Free Sizing Review</h4>
        <p class="copy">A technician checks your gas line, venting and household demand, then quotes the right tankless unit at the best price in Palm Beach County.</p>
      </div>
    </div>
  </section>
  <section class="panel contact-card">
    <h2 class="section-title">Contact Details</h2>
    <div class="contact-row">
      <div class="map" role="img" aria-label="Small map of Palm Beach County, Florida"></div>
      <p class="copy">Serving homes and businesses across Palm Beach County. Call for same-day service, seven days a week.</p>
    </div>
  </section>
</article>

<!-- Privacy & terms page -->
<article class="page page-legal">
  <header class="site-header">
    <span class="brand"><i class="brand-dot"></i>Sir FlowBoiler</span>
    <nav class="main-nav"><span class="active">Home</span><span>Gas</span><span>Electric</span><span>About</span></nav>
    <svg class="search-icon" viewBox="0 0 10 10"><circle cx="4" cy="4" r="3" fill="none" stroke="#10233f"/><path d="M6.2 6.2 9 9" stroke="#10233f"/></svg>
    <span class="btn-quote">Get a Quote</span>
  </header>
  <section class="hero hero-legal">
    <div class="hero-bg" role="img" aria-label="Suburban street, softly blurred"></div>
    <div class="van-photo" role="img" aria-label="Photo of a white service van and a plumber in work uniform"></div>
    <div class="quote-form">
      <h1>Get Water Heater<br>Today!</h1>
      <p class="form-label">Request a quote</p>
      <div class="form-input">Your full name</div>
      <div class="form-input">Phone number</div>
      <div class="form-input">Service needed</div>
    </div>
  </section>
  <div class="cta-row"><span class="btn btn-primary">Request Same-Day Water Heater Service Now</span><span class="link">Call Today</span></div>
  <div class="trust-row">
    <div class="trust"><svg viewBox="0 0 10 10"><circle cx="5" cy="5" r="4.5" fill="#EE7325"/></svg>Same-Day<br>Service</div>
    <div class="trust"><svg viewBox="0 0 10 10"><circle cx="5" cy="5" r="4.5" fill="#EE7325"/></svg>Best Price<br>Guarantee</div>
    <div class="trust"><svg viewBox="0 0 10 10"><circle cx="5" cy="5" r="4.5" fill="#EE7325"/></svg>Lifetime<br>Workmanship</div>
  </div>
  <div class="legal-grid">
    <section class="panel legal-card">
      <h2 class="section-title">Privacy Policy</h2>
      <p class="copy">We collect only the details you share through our quote and newsletter forms, such as your name, phone number, email and service address.</p>
      <p class="copy">This information is used to schedule visits, send estimates and follow up on warranty service. We never sell your data to third parties.</p>
      <p class="copy">You may ask us to update or delete your records at any time by contacting our office.</p>
      <span class="btn-orange">Learn More Details</span>
    </section>
    <section class="panel legal-card">
      <h2 class="section-title">Terms &amp; Free &amp; Conditions</h2>
      <p class="copy">All quotes are valid for thirty days. Same-day service depends on technician availability and the time of your call.</p>
      <div class="notice-box">
        <strong>Warranty Coverage Terms</strong>
        <p class="copy">Heater and parts carry a 15-year warranty. Workmanship is covered for life. All warranties transfer upon home sale.</p>
      </div>
      <p class="copy">Payment is due when work is complete unless other terms are agreed in writing.</p>
    </section>
    <section class="panel legal-card short">
      <h2 class="section-title">Warranty Policy</h2>
      <div class="warranty-photo photo" role="img" aria-label="Photo of a technician in blue uniform in a bright room"></div>
    </section>
    <section class="panel legal-card short">
      <h2 class="section-title">Terms &amp; Conditions</h2>
      <p class="copy">Customers must provide safe access to the water heater location. Permits and disposal of old tanks are included in every installation quote we provide.</p>
      <p class="copy">Our best price guarantee matches any written local quote for the same model and scope of work.</p>
    </section>
  </div>
</article>

</body>
</html>
```